OM sidrawi Multibrand Web Design

We need Simple but very Elegant Website for Our Middle East Company based in Kuwait, We are not good in describing design but we need simple but elegant and responsive to attract new market and to enable us competing in business

It Company

```html
<!DOCTYPE html>
<html lang="en">
<head>
<meta charset="utf-8">
<title>OM sidrawi</title>
<link rel="stylesheet" href="https://fonts.googleapis.com/css2?family=Playfair+Display:wght@700&family=Roboto:wght@300;400;500;700&family=Lora:ital@1&display=swap">
<style>
:root{
  --ink:#111111;
  --text:#555555;
  --muted:#8a8a8a;
  --line:#dddddd;
  --white:#ffffff;
  --soft:#f4f4f4;
  --black:#050505;
  --night-1:#1a1424;
  --night-2:#2a2030;
  --city-glow:#6a4a2e;
  --video-1:#2b2219;
  --video-2:#0f0c09;
}
*{box-sizing:border-box;margin:0;padding:0}
html,body{width:1200px;height:2381px;overflow:hidden}
body{font-family:"Roboto",Arial,sans-serif;color:var(--text);background:var(--white);position:relative}
.wrap{position:absolute;left:246px;width:706px}
.serif{font-family:"Playfair Display",Georgia,serif}

/* Hero */
.hero{position:absolute;top:0;left:0;width:1200px;height:502px;overflow:hidden}
.hero-photo{position:absolute;inset:0;background:
  linear-gradient(180deg,var(--night-1) 0%,var(--night-2) 45%,#3a2a2a 62%,var(--city-glow) 78%,#141018 90%,#0c0a10 100%)}
.nav{position:absolute;top:0;left:246px;width:706px;height:60px;display:flex;align-items:center;justify-content:space-between}
.brand{color:var(--white);font-size:22px;font-weight:400;letter-spacing:.2px}
.menu{display:flex;gap:0;list-style:none}
.menu li{font-size:10.5px;font-weight:700;color:var(--white);text-transform:uppercase;padding:0 12px;height:48px;display:flex;align-items:center;position:relative}
.menu li.active::after{content:"";position:absolute;left:0;right:0;bottom:0;height:2px;background:var(--white)}
.menu li:last-child{padding-right:0}
.hero-copy{position:absolute;top:164px;left:300px;width:600px;text-align:center;color:var(--white)}
.hero-copy h1{font-size:24px;line-height:30px}
.hero-copy p{margin-top:24px;font-size:11.5px;line-height:19px;font-weight:400}
.btn-ghost{display:inline-block;margin-top:26px;border:1px solid var(--white);color:var(--white);font-size:11px;padding:8px 12px;text-transform:uppercase}
.dots{position:absolute;top:442px;left:0;width:1200px;display:flex;justify-content:center;gap:4px}
.dots span{width:7px;height:7px;border-radius:50%;border:1px solid var(--white)}
.dots span.on{background:var(--white)}

/* Story */
.story{position:absolute;top:502px;left:0;width:1200px;height:301px;text-align:center}
.story h2{position:absolute;top:48px;width:1200px;font-size:16px;color:var(--ink);letter-spacing:.8px}
.story .copy{position:absolute;top:96px;left:306px;width:588px;font-size:11px;line-height:18px;color:var(--muted)}
.story .copy p+p{margin-top:14px}
.btn-line{position:absolute;top:220px;left:555px;border:1px solid var(--ink);color:var(--ink);font-size:11px;padding:8px 12px;text-transform:uppercase}

/* Video */
.video{position:absolute;top:803px;left:0;width:1200px;height:413px;background:radial-gradient(ellipse at 75% 70%,#6a4a28 0%,transparent 45%),linear-gradient(160deg,var(--video-1),var(--video-2))}
.play{position:absolute;left:561px;top:955px}
.video-label{position:absolute;top:1052px;left:0;width:1200px;text-align:center;color:var(--white);font-size:12px;font-weight:700;text-transform:uppercase;letter-spacing:.3px}

/* Testimonial */
.quotes{position:absolute;top:1216px;left:0;width:1200px;height:376px;background:var(--soft);text-align:center}
.quote-mark{position:absolute;top:42px;width:1200px;font-family:"Playfair Display",Georgia,serif;font-size:40px;color:#444}
.quote-text{position:absolute;top:94px;left:300px;width:600px;font-family:"Lora",Georgia,serif;font-style:italic;font-size:11.5px;line-height:20px;color:#444}
.who{position:absolute;top:208px;width:1200px;font-size:10.5px;color:#333;letter-spacing:.6px;text-transform:uppercase}
.who-role{position:absolute;top:226px;width:1200px;font-size:9px;color:var(--muted);text-transform:uppercase}
.avatars{position:absolute;top:268px;left:448px;width:304px;height:56px;display:flex;align-items:center;justify-content:space-between}
.avatar{width:34px;height:34px;border-radius:50%;border:2px solid var(--white);background:linear-gradient(135deg,#c9a88a,#6e5546)}
.avatar.big{width:50px;height:50px;background:linear-gradient(135deg,#d8b8a0,#8a3a3a)}
.arrow{width:14px;height:20px}

/* Contact & clients */
.contact{position:absolute;top:1592px;left:0;width:1200px;height:489px}
.contact h3{font-family:"Playfair Display",Georgia,serif;font-size:16px;color:var(--ink);letter-spacing:.8px;position:absolute;top:48px}
.form{position:absolute;left:246px;width:346px}
.field{position:absolute;left:0;width:346px;height:33px;border:1px solid var(--line);font-size:10.5px;color:#aaa;padding:10px 14px}
.field.area{height:149px}
.submit{position:absolute;left:0;top:406px;width:90px;height:29px;background:var(--black);color:var(--white);font-size:10.5px;font-weight:500;text-transform:uppercase;display:flex;align-items:center;justify-content:center}
.clients{position:absolute;left:667px;width:285px}
.client{position:absolute;font-family:"Roboto",Arial,sans-serif;font-weight:500;font-size:17px;color:var(--ink);letter-spacing:.5px;display:flex;align-items:center;gap:8px}
.client i{display:inline-block;width:10px;height:10px;background:var(--ink)}

/* Footer */
.footer{position:absolute;top:2081px;left:0;width:1200px;height:300px;background:var(--black);color:var(--white)}
.f-brand{position:absolute;top:58px;left:246px;font-size:20px;font-weight:300}
.f-about{position:absolute;top:104px;left:246px;width:230px;font-size:10.5px;line-height:20px}
.f-head{position:absolute;top:67px;font-size:10.5px;font-weight:700;text-transform:uppercase;letter-spacing:.4px}
.f-row{position:absolute;left:487px;display:flex;gap:12px;font-size:10.5px;line-height:19px}
.f-row svg{flex:none;margin-top:3px}
.subscribe{position:absolute;top:105px;left:733px;width:159px;height:33px;border:1px solid #888;font-size:10.5px;padding:10px 12px}
.send{position:absolute;top:105px;left:900px;width:52px;height:33px;background:var(--white);display:flex;align-items:center;justify-content:center}
.socials{position:absolute;top:157px;left:733px;display:flex;gap:7px}
.socials span{width:26px;height:26px;border-radius:50%;border:1px solid var(--white)}
.f-links{position:absolute;top:234px;left:246px;display:flex;gap:22px;font-size:10.5px;text-transform:uppercase}
.copyright{position:absolute;top:234px;right:248px;font-size:10.5px}
</style>
</head>
<body>

<header class="hero">
  <div class="hero-photo" role="img" aria-label="Night skyline of a waterfront city with lit towers reflected in the water"></div>
  <nav class="nav">
    <div class="brand">OM sidrawi</div>
    <ul class="menu">
      <li class="active">Home</li>
      <li>About</li>
      <li>People Say</li>
      <li>Contact</li>
    </ul>
  </nav>
  <div class="hero-copy">
    <h1 class="serif">We Are Reliable Company Based In Kuwait</h1>
    <p>Lorem Ipsum. Proin gravida nibh vel velit auctor aliquet. Aenean sollicitudin, lorem quis bibendum auctor, nisi elit consequat ipsum, nec sagittis sem nibh id elit. Duis sed odio sit amet nibh vulputate cursus a sit amet mauris. Morbi accumsan ipsum velit.</p>
    <span class="btn-ghost">Learn More</span>
  </div>
  <div class="dots"><span class="on"></span><span></span><span></span><span></span></div>
</header>

<section class="story">
  <h2 class="serif">OUR STORY</h2>
  <div class="copy">
    <p>This is Photoshop's version of Lorem Ipsum. Proin gravida nibh vel velit auctor aliquet. Aenean sollicitudin, lorem quis bibendum auctor, nisi elit consequat ipsum, nec sagittis sem nibh id elit. Duis sed odio sit amet nibh vulputate cursus</p>
    <p>Morbi accumsan ipsum velit. Nam nec tellus a odio tincidunt auctor a ornare odio. Sed non mauris vitae erat consequat auctor eu in elit. Class aptent taciti sociosqu ad litora torquent per conubia nostra, per inceptos himenaeos.</p>
  </div>
  <span class="btn-line">Learn More</span>
</section>

<section class="video" role="img" aria-label="Aerial night view of downtown towers and a lit highway"></section>
<svg class="play" width="78" height="78" viewBox="0 0 78 78" aria-hidden="true">
  <circle cx="39" cy="39" r="36" fill="none" stroke="#fff" stroke-width="2"/>
  <path d="M31 26 L54 39 L31 52 Z" fill="none" stroke="#fff" stroke-width="2" stroke-linejoin="round"/>
</svg>
<div class="video-label">Watch Our Company Profile</div>

<section class="quotes">
  <div class="quote-mark">&ldquo;</div>
  <p class="quote-text">This is Photoshop's version of Lorem Ipsum. Proin gravida nibh vel velit auctor aliquet. Aenean sollicitudin, lorem quis bibendum auctor, nisi elit consequat ipsum, nec sagittis sem nibh id elit. Duis sed odio sit amet nibh vulputate cursus a sit amet mauris. Morbi accumsan ipsum velit. Nam nec tellus a odio tincidunt auctor a ornare odio. Sed non mauris vitae erat consequat auctor eu in elit.</p>
  <div class="who">Mira Castell</div>
  <div class="who-role">CEO Harbourline</div>
  <div class="avatars">
    <svg class="arrow" viewBox="0 0 14 20" aria-hidden="true"><path d="M10 3 L4 10 L10 17" fill="none" stroke="#999" stroke-width="1.5"/></svg>
    <span class="avatar" role="img" aria-label="Client portrait"></span>
    <span class="avatar" role="img" aria-label="Client portrait"></span>
    <span class="avatar big" role="img" aria-label="Portrait of the quoted client"></span>
    <span class="avatar" role="img" aria-label="Client portrait"></span>
    <span class="avatar" role="img" aria-label="Client portrait"></span>
    <svg class="arrow" viewBox="0 0 14 20" aria-hidden="true"><path d="M4 3 L10 10 L4 17" fill="none" stroke="#999" stroke-width="1.5"/></svg>
  </div>
</section>

<section class="contact">
  <h3 style="left:246px">GIVE US A GOOD NEWS</h3>
  <div class="form" style="top:89px">
    <div class="field" style="top:0">Name</div>
    <div class="field" style="top:51px">Email</div>
    <div class="field" style="top:100px">Subject</div>
    <div class="field area" style="top:152px">Your Massage</div>
    <div class="submit" style="top:317px">Submit</div>
  </div>
  <h3 style="left:667px">OUR HAPPY CLIENT</h3>
  <div class="clients" style="top:0">
    <div class="client" style="left:0;top:96px">Verano</div>
    <div class="client" style="left:179px;top:96px">Solenne</div>
    <div class="client" style="left:0;top:155px">Halden &amp; Vale</div>
    <div class="client" style="left:179px;top:155px">Corvia</div>
    <div class="client" style="left:0;top:215px">Linnet Moda</div>
    <div class="client" style="left:179px;top:215px">Stridely</div>
    <div class="client" style="left:0;top:288px"><i></i>Northpace</div>
    <div class="client" style="left:179px;top:288px">Kestrel</div>
    <div class="client" style="left:0;top:366px">Denholt</div>
    <div class="client" style="left:179px;top:366px">Tidewell</div>
  </div>
</section>

<footer class="footer">
  <div class="f-brand">OM sidrawi</div>
  <p class="f-about">lorem quis bibendum auctor, nisi elit consequat ipsum, nec sagittis sem nibh elit. Duis sed odio sit amet auctror a ornare odio non mauris vitae erat in elit</p>

  <div class="f-head" style="left:487px">Our Studio</div>
  <div class="f-row" style="top:104px">
    <svg width="12" height="14" viewBox="0 0 12 14" aria-hidden="true"><path d="M6 13 C2 8 1 6.5 1 5 A5 5 0 0 1 11 5 C11 6.5 10 8 6 13 Z" fill="none" stroke="#fff"/><circle cx="6" cy="5" r="1.7" fill="none" stroke="#fff"/></svg>
    <div>Name of Street 12<br>Name of City<br>United Arab</div>
  </div>
  <div class="f-row" style="top:170px">
    <svg width="12" height="12" viewBox="0 0 12 12" aria-hidden="true"><path d="M2.5 1 L4.5 1 L5.5 3.5 L4 4.5 A7 7 0 0 0 7.5 8 L8.5 6.5 L11 7.5 L11 9.5 A1.5 1.5 0 0 1 9.5 11 A9 9 0 0 1 1 2.5 A1.5 1.5 0 0 1 2.5 1 Z" fill="none" stroke="#fff"/></svg>
    <div>(+965) 21-5508 1470</div>
  </div>

  <div class="f-head" style="left:733px">Stay In Touch</div>
  <div class="subscribe">Subscribe our newsletter</div>
  <div class="send">
    <svg width="16" height="16" viewBox="0 0 16 16" aria-hidden="true"><path d="M1 7 L15 1 L10 15 L7.5 9 Z M7.5 9 L15 1" fill="none" stroke="#111" stroke-width="1.2" stroke-linejoin="round"/></svg>
  </div>
  <div class="socials"><span></span><span></span><span></span><span></span><span></span></div>

  <div class="f-links"><span>Help</span><span>Terms &amp; Condition</span><span>Privacy</span></div>
  <div class="copyright">Copyright &copy; 2018 - OM sidrawi</div>
</footer>

</body>
</html>
```